Criação de Layout Web-Design para Decoração & Mobília
" Produzimos sofas, poltronas e puff de alta qualidade, com produção customizada para cada cliente. Atendemos clientes em todo território nacional, através de nossos representantes comerciais ou por meio eletrônico diretamente com a fabrica. Trabalhamos com as melhores materias primas do mercado e temos uma linha de tecidos importada que transformam os estofados em produtos exclusivos e de alta qualidade. "

```html
<!DOCTYPE html>
<html lang="pt-BR">
<head>
<meta charset="UTF-8">
<title>Nara — Quem Somos</title>
<link rel="stylesheet" href="https://fonts.googleapis.com/css2?family=Raleway:wght@400;500;600&display=swap">
<style>
  :root {
    --header-bg: #1b1b1b;
    --header-line: #2c2c2c;
    --nav-text: #e9e9e9;
    --nav-active: #9a9a9a;
    --accent: #b89a5e;
    --page-bg: #f4f4f4;
    --panel-bg: #ebebeb;
    --panel-edge: #dddddd;
    --heading: #3a3a3a;
    --body-text: #6e6e6e;
    --rule: #d3c6a8;
  }
  * { box-sizing: border-box; margin: 0; padding: 0; }
  html, body {
    width: 1200px; height: 1200px; overflow: hidden;
    background: var(--page-bg);
    font-family: "Raleway", sans-serif;
  }
  .site { width: 1200px; height: 1200px; display: flex; flex-direction: column; }

  .site-header {
    height: 132px; background: var(--header-bg);
    border-bottom: 1px solid var(--header-line);
    display: flex; align-items: center; justify-content: space-between;
    padding: 0 64px;
  }
  .brand {
    font-size: 30px; font-weight: 500; color: var(--nav-text);
    letter-spacing: 2px; text-transform: uppercase; line-height: 1;
    margin-top: 24px;
  }
  .main-nav { display: flex; align-items: center; gap: 28px; margin-top: -40px; }
  .main-nav a {
    color: var(--nav-text); text-decoration: none;
    font-size: 14px; font-weight: 500; letter-spacing: .5px; text-transform: uppercase;
    white-space: nowrap;
  }
  .main-nav a.is-active { color: var(--nav-active); }
  .nav-divider { width: 1px; height: 16px; background: #555; }
  .search-icon { width: 18px; height: 18px; }

  .content { flex: 1; padding: 36px 64px 0; display: flex; flex-direction: column; }

  .section-title {
    font-size: 15px; font-weight: 600; color: var(--accent);
    letter-spacing: 1px; text-transform: uppercase;
    padding-bottom: 14px; border-bottom: 1px solid var(--rule);
    margin-bottom: 32px;
  }

  .about-panel {
    background: var(--panel-bg); border: 1px solid var(--panel-edge);
    padding: 44px;
    display: flex; gap: 40px; align-items: flex-start;
  }
  .about-text { flex: 1; padding-top: 8px; }
  .about-heading {
    font-size: 18px; font-weight: 500; color: var(--heading);
    text-transform: uppercase; letter-spacing: .3px; white-space: nowrap;
    padding-bottom: 16px; border-bottom: 1px solid #cfcfcf; margin-bottom: 26px;
  }
  .about-copy {
    font-size: 15px; font-weight: 400; line-height: 1.8; color: var(--body-text);
  }
  .about-photo {
    width: 460px; height: 360px; flex-shrink: 0;
    background: linear-gradient(180deg, #c9c3b9 0%, #e8e4dc 38%, #bdb2a2 60%, #4a4540 100%);
    box-shadow: 0 2px 6px rgba(0,0,0,.15);
  }

  .team-panel {
    margin-top: 44px; flex: 1;
    background: var(--panel-bg); border: 1px solid var(--panel-edge); border-bottom: none;
    padding: 26px 28px 0;
  }
  .team-title {
    font-size: 15px; font-weight: 600; color: var(--heading);
    text-transform: uppercase; letter-spacing: 1px;
    padding-bottom: 12px; border-bottom: 1px solid #cfcfcf; margin-bottom: 22px;
  }
  .team-row { display: flex; gap: 24px; }
  .team-photo {
    flex: 1; height: 260px;
    background: linear-gradient(180deg, #d8d3cb 0%, #b9b2a7 100%);
  }
</style>
</head>
<body>
<div class="site">
  <header class="site-header">
    <div class="brand">Nara</div>
    <nav class="main-nav">
      <a href="#" class="is-active">Home</a>
      <a href="#">Produtos</a>
      <a href="#">Novidades</a>
      <span class="nav-divider"></span>
      <a href="#">Loja Virtual</a>
      <span class="nav-divider"></span>
      <a href="#">Representantes</a>
      <span class="nav-divider"></span>
      <a href="#">Fale Conosco</a>
      <svg class="search-icon" viewBox="0 0 18 18" aria-label="Buscar">
        <circle cx="7.5" cy="7.5" r="5.5" fill="none" stroke="#e9e9e9" stroke-width="2"/>
        <line x1="11.5" y1="11.5" x2="16.5" y2="16.5" stroke="#e9e9e9" stroke-width="2" stroke-linecap="round"/>
      </svg>
    </nav>
  </header>

  <main class="content">
    <h2 class="section-title">Quem Somos</h2>

    <section class="about-panel">
      <div class="about-text">
        <h3 class="about-heading">Somos apaixonados pelo que vendemos</h3>
        <p class="about-copy">Nós somos apaixonados por tornar o mobiliário urbano acessível para todos os entusiastas modernos. Sem limitações básicas. Trabalhamos com uma equipe selecionada à mão de designers de todo o mundo para criar peças inovadoras que são elegantes, sofisticadas e meticulosamente criadas. Estas silhuetas contemporâneas, linhas elegantes e acabamentos brilhantes que você ama são finalmente acessíveis. Confira a mesa de centro com a qual você sonhou. Nós fizemos isso apenas para você.</p>
      </div>
      <div class="about-photo" role="img" aria-label="Fotografia de sala de estar com sofás e poltronas claros, mesa de centro de madeira e tapete"></div>
    </section>

    <section class="team-panel">
      <h3 class="team-title">Nossa Equipe</h3>
      <div class="team-row">
        <div class="team-photo" role="img" aria-label="Foto de membro da equipe"></div>
        <div class="team-photo" role="img" aria-label="Foto de membro da equipe"></div>
        <div class="team-photo" role="img" aria-label="Foto de membro da equipe"></div>
        <div class="team-photo" role="img" aria-label="Foto de membro da equipe"></div>
      </div>
    </section>
  </main>
</div>
</body>
</html>
```